KIDS CONSIGNMENT STORE

I need a design for my new store advertising. I just opened about a month ago. The store name PEBBLES IN A POCKET. I have gently used childrens clothes, toys and baby things. Strollers, furnitures, highchair, swing, walker, clothes, shoes, toys, accessories. Nursury things..... Name brand clothes, VEX, BRANDT OSWELLY, SPROUTLING DEPOT, VELMA ROUSSIN, MABEL AND FINCH,RUVA, GLEN HOPPA, VERANDIX, QUIRA..ETC... I already have the store logo,see attachment! I would like to have flyers what is eye catching, colorful, nice AND BRINGS A LOT OF CUSTOMERS!!!! :-) I need adress and phone number on it of course, and LIKE US ON CHATNEST!!!! I would like to drop them off in local businesses and schools, libarys, etc etc.....

```html
<!DOCTYPE html>
<html lang="en">
<head>
<meta charset="utf-8">
<title>Pebbles In A Pocket – Postcard</title>
<link rel="stylesheet" href="https://fonts.googleapis.com/css2?family=Comic+Neue:wght@400;700&family=Archivo:wght@800&family=Lato:wght@700&display=swap">
<style>
  :root {
    --backdrop: #3a3a3a;
    --wood-dark: #4e2a1e;
    --wood-light: #7a4330;
    --grass: #6fa63a;
    --tangerine: #f07a1a;
    --sky: #29abe2;
    --panel-blue: #4aa3dd;
    --sun: #fcc419;
    --cherry: #e4232b;
    --navy: #2e3d91;
    --ink: #222222;
    --soft-ink: #3a3a3a;
    --paper: #ffffff;
    --logo-black: #111111;
  }
  * { margin: 0; padding: 0; box-sizing: border-box; }
  html, body { width: 907px; height: 1200px; overflow: hidden; }
  body { background: var(--backdrop); position: relative; font-family: "Comic Neue", "Comic Sans MS", cursive; }

  .card { position: absolute; overflow: hidden; background: var(--paper); }
  .card svg.shapes { position: absolute; inset: 0; }

  /* Front */
  .card-front { left: 110px; top: 40px; width: 690px; height: 533px; }
  .logo-block {
    position: absolute; display: flex; align-items: center; justify-content: center;
    background: var(--logo-black); color: var(--paper); text-align: center;
    font-family: "Comic Neue", "Comic Sans MS", cursive; font-weight: 700; line-height: 1.1;
  }
  .card-front .logo-block { left: 17px; top: 15px; width: 165px; height: 165px; font-size: 24px; padding: 12px; }
  .front-title { position: absolute; right: 30px; top: 322px; text-align: right; }
  .front-title .small { display: block; font-family: "Comic Neue", "Comic Sans MS", cursive; font-weight: 700; font-size: 44px; color: var(--paper); line-height: 1; }
  .front-title .big { display: block; font-family: "Archivo", "Arial Black", sans-serif; font-weight: 800; font-size: 66px; line-height: 1; letter-spacing: -1px; }
  .front-title .red { color: var(--cherry); }
  .front-title .blue { color: var(--navy); }

  /* Back */
  .card-back { left: 113px; top: 615px; width: 687px; height: 530px; }
  .back-title { position: absolute; right: 347px; top: 158px; text-align: right; }
  .back-title .small { display: block; font-size: 28px; color: var(--soft-ink); line-height: 1.1; }
  .back-title .big { display: block; font-family: "Archivo", "Arial Black", sans-serif; font-weight: 800; font-size: 28px; color: var(--cherry); line-height: 1.1; }
  .shop-copy {
    position: absolute; left: 18px; top: 237px; width: 335px;
    font-size: 14.2px; line-height: 18.2px; color: var(--paper);
  }
  .contact-list { position: absolute; left: 22px; top: 410px; list-style: none; }
  .contact-list li { display: flex; align-items: center; height: 25px; font-family: "Lato", sans-serif; font-weight: 700; font-size: 15px; color: var(--ink); white-space: nowrap; }
  .contact-list svg { width: 16px; height: 16px; margin-right: 9px; flex: none; }
  .social { display: flex; align-items: center; margin-top: 3px; height: 30px !important; }
  .social .dot { width: 28px; height: 28px; background: var(--navy); margin-right: 8px; flex: none; }
  .social .label { font-family: "Lato", sans-serif; font-weight: 700; color: var(--navy); line-height: 1; }
  .social .label small { display: block; font-size: 12px; color: var(--ink); }
  .social .label span { font-size: 16px; }
  .card-back .logo-block { left: 254px; top: 423px; width: 83px; height: 82px; font-size: 12px; padding: 6px; }
  .stamp-box { position: absolute; left: 603px; top: 114px; width: 46px; height: 56px; border: 1.5px solid var(--ink); }
  .address-line { position: absolute; left: 454px; width: 199px; height: 1.5px; background: var(--ink); }
</style>
</head>
<body>

<section class="card card-front">
  <svg class="shapes" width="690" height="533" viewBox="0 0 690 533">
    <defs>
      <linearGradient id="woodTone" x1="0" y1="0" x2="1" y2="1">
        <stop offset="0" stop-color="var(--wood-light)"/>
        <stop offset="1" stop-color="var(--wood-dark)"/>
      </linearGradient>
      <linearGradient id="winterTone" x1="0" y1="0" x2="1" y2="1">
        <stop offset="0" stop-color="#e9c3d8"/>
        <stop offset="1" stop-color="#cfe3f2"/>
      </linearGradient>
    </defs>
    <rect class="hero-photo" width="690" height="533" fill="url(#woodTone)" role="img" aria-label="Photo of two smiling girls in knitted winter hats and sweaters against a wooden wall"/>
    <path class="grass-wave" d="M0 265 C120 330 300 365 400 352 C520 336 600 282 690 272 L690 533 L0 533 Z" fill="var(--grass)"/>
    <path class="orange-ribbon" d="M360 362 C480 332 590 262 690 250 L690 272 C600 282 520 336 400 352 Z" fill="var(--tangerine)"/>
    <path class="inset-photo" d="M60 300 C100 240 230 225 300 250 C360 270 385 320 362 370 C340 420 262 420 232 460 C202 505 122 510 82 490 C42 470 40 340 60 300 Z"
          fill="url(#winterTone)" stroke="var(--sky)" stroke-width="6" role="img" aria-label="Photo of two young children in pink knitted hats and scarves"/>
  </svg>
  <div class="logo-block">PEBBLES IN A POCKET</div>
  <h1 class="front-title">
    <span class="small">Pebbles</span>
    <span class="big red">In A</span>
    <span class="big blue">Pocket</span>
  </h1>
</section>

<section class="card card-back">
  <svg class="shapes" width="687" height="530" viewBox="0 0 687 530">
    <path class="blue-panel" d="M0 75 C60 110 120 160 190 162 C260 165 330 140 355 80 L355 385 C220 402 100 398 0 378 Z" fill="var(--panel-blue)"/>
    <path class="yellow-ribbon" d="M190 150 C270 150 340 110 355 50 L355 80 C330 140 260 165 190 162 Z" fill="var(--sun)"/>
    <path class="baby-photo" d="M18 60 C40 20 140 15 190 30 C230 42 232 90 200 110 C170 130 120 120 105 150 C90 185 50 200 30 185 C5 165 2 100 18 60 Z"
          fill="#b9a3b8" stroke="var(--paper)" stroke-width="6" role="img" aria-label="Photo of a baby in a knitted hat and scarf"/>
    <path d="M12 58 C36 12 142 6 194 22 C240 36 242 94 205 117 C176 135 128 126 113 154 C96 192 52 210 26 192 C-4 170 -4 98 12 58 Z"
          fill="none" stroke="var(--cherry)" stroke-width="7"/>
  </svg>

  <h2 class="back-title">
    <span class="small">Pebbles In A</span>
    <span class="big">POCKET</span>
  </h2>

  <p class="shop-copy">I have gently used childrens clothes, toys and baby things. Strollers, furnitures, highchair, swing, walker, clothes, shoes, toys, accessories. Nursury things..... Name brand clothes, VEX, BRANDT OSWELLY, SPROUTLING DEPOT, VELMA ROUSSIN, MABEL AND FINCH, RUVA, GLEN HOPPA, VERANDIX, QUIRA..ETC..</p>

  <ul class="contact-list">
    <li>
      <svg viewBox="0 0 16 16"><path d="M3 1 L6 1 L7 5 L5 6.5 C6 9 7 10 9.5 11 L11 9 L15 10 L15 13 C15 14 14 15 13 15 C6 15 1 10 1 3 C1 2 2 1 3 1 Z" fill="var(--ink)"/></svg>
      555-014-2280
    </li>
    <li>
      <svg viewBox="0 0 16 16"><path d="M8 1 C5 1 3 3.2 3 6 C3 9.5 8 15 8 15 C8 15 13 9.5 13 6 C13 3.2 11 1 8 1 Z" fill="var(--ink)"/><circle cx="8" cy="6" r="2" fill="var(--paper)"/></svg>
      218 Maple Row, Brookfield
    </li>
    <li>
      <svg viewBox="0 0 16 16"><circle cx="8" cy="8" r="6.5" fill="none" stroke="var(--ink)" stroke-width="1.8"/><path d="M1.5 8 H14.5 M8 1.5 C5 5 5 11 8 14.5 M8 1.5 C11 5 11 11 8 14.5" fill="none" stroke="var(--ink)" stroke-width="1.4"/></svg>
      www.pebblespocket.shop
    </li>
    <li class="social">
      <span class="dot"></span>
      <span class="label"><small>Like us on</small><span>CHATNEST</span></span>
    </li>
  </ul>

  <div class="logo-block">PEBBLES IN A POCKET</div>

  <div class="stamp-box"></div>
  <div class="address-line" style="top:280px"></div>
  <div class="address-line" style="top:305px"></div>
  <div class="address-line" style="top:330px"></div>
</section>

</body>
</html>
```